Ridgeway Fruit Depot Logo/Label Design

I am designing a blueberry label that will be placed on clam shells when the fruit is packed. The label will the company name "The Ridgeway Fruit Depot". It will also list Blueberries/Bleuets (Blueberries in French). It small print it would say Dist. By/Par The Ridgeway Fruit Depot, Corliss, GA 30874 USA. It would also list the package size. 1 US Dry Pint/1 Chopine Seche US 551 ml. I have provided some sample labels that other marketers use.

```html
<!DOCTYPE html>
<html lang="en">
<head>
<meta charset="utf-8">
<title>The Ridgeway Fruit Depot – Blueberry Label</title>
<link rel="stylesheet" href="https://fonts.googleapis.com/css2?family=Montserrat:wght@500;600;800&family=Pacifico&display=swap">
<style>
  :root {
    --page-bg: #e6eef8;
    --navy: #1c2a6e;
    --navy-deep: #1a1f5c;
    --stripe: #3b7fe3;
    --sky-top: #5fb8ef;
    --sky-bottom: #3f8ad8;
    --wave: #8fdaf4;
    --paper: #ffffff;
    --ring: #7ccaf0;
    --berry-light: #5f82ad;
    --berry-dark: #2a3f63;
    --brand-text: #6cc0f0;
    --script: #ffffff;
    --small-text: #3b3f5c;
    --size-text: #6f88b8;
  }
  * { margin: 0; padding: 0; box-sizing: border-box; }
  html, body { width: 1200px; height: 858px; overflow: hidden; }
  body { background: var(--page-bg); position: relative; font-family: "Montserrat", sans-serif; }

  .label {
    position: absolute; left: 60px; top: 159px;
    width: 1080px; height: 540px;
    border-radius: 58px; overflow: hidden;
    box-shadow: 0 18px 40px rgba(30, 50, 90, 0.18);
  }
  .label-art { position: absolute; inset: 0; width: 100%; height: 100%; display: block; }

  .brand-name {
    position: absolute; left: 0; width: 660px; top: 12px;
    text-align: center; color: var(--brand-text);
    font-weight: 800; font-size: 44px; line-height: 46px; letter-spacing: 0.5px;
  }

  .product-name {
    position: absolute; left: 0; width: 650px; text-align: center;
    font-family: "Pacifico", cursive; color: var(--script);
    font-size: 100px; line-height: 1;
  }
  .product-name.english { top: 128px; }
  .product-name.french { top: 272px; }

  .divider {
    position: absolute; left: 23px; width: 596px; top: 272px; height: 4px;
    background: linear-gradient(90deg, rgba(255,255,255,0.3), rgba(255,255,255,0.85) 30%, rgba(255,255,255,0.85) 70%, rgba(255,255,255,0.3));
    border-radius: 2px;
  }

  .fine-print {
    position: absolute; left: 0; width: 670px; top: 451px;
    text-align: center; color: var(--small-text);
    font-weight: 500; font-size: 20px; line-height: 23px;
  }
  .package-size {
    position: absolute; left: 0; width: 670px; top: 503px;
    text-align: center; color: var(--size-text);
    font-weight: 600; font-size: 16.5px;
  }
</style>
</head>
<body>
  <div class="label">
    <svg class="label-art" viewBox="0 0 1080 540" xmlns="http://www.w3.org/2000/svg">
      <defs>
        <linearGradient id="sky" x1="0" y1="0" x2="1" y2="1">
          <stop offset="0" stop-color="var(--sky-top)"/>
          <stop offset="1" stop-color="var(--sky-bottom)"/>
        </linearGradient>
        <linearGradient id="navy" x1="0" y1="0" x2="1" y2="0">
          <stop offset="0" stop-color="var(--navy)"/>
          <stop offset="1" stop-color="var(--navy-deep)"/>
        </linearGradient>
        <radialGradient id="berries" cx="0.55" cy="0.45" r="0.75">
          <stop offset="0" stop-color="var(--berry-light)"/>
          <stop offset="1" stop-color="var(--berry-dark)"/>
        </radialGradient>
      </defs>
      <rect class="sky-field" width="1080" height="540" fill="url(#sky)"/>
      <path class="accent-stripe" d="M0 64 C260 140 560 140 780 92 L780 112 C560 160 260 160 0 84 Z" fill="var(--stripe)"/>
      <path class="top-band" d="M0 0 H800 V92 C560 136 260 132 0 68 Z" fill="url(#navy)"/>
      <path class="bottom-wave" d="M0 412 C240 392 480 402 720 436 V540 H0 Z" fill="var(--wave)"/>
      <path class="bottom-panel" d="M0 460 C240 428 480 430 720 450 V540 H0 Z" fill="var(--paper)"/>
      <path class="photo-ring" d="M705 0 C632 150 628 400 690 540 H1080 V0 Z" fill="var(--ring)"/>
      <g role="img" aria-label="Close-up photograph of fresh blueberries">
        <path class="photo-area" d="M735 0 C666 150 660 400 726 540 H1080 V0 Z" fill="url(#berries)"/>
      </g>
    </svg>

    <div class="brand-name">The Ridgeway<br>Fruit Depot</div>

    <div class="product-name english">Blueberries</div>
    <div class="divider"></div>
    <div class="product-name french">Bleuets</div>

    <p class="fine-print">Dist. By / Par The Ridgeway Fruit Depot,<br>Corliss, GA 30874 USA</p>
    <p class="package-size">1 US Dry Pint / 1 Chopine Sèche US 551 ml</p>
  </div>
</body>
</html>
```